Label for Cartridge for water filter cartridge

Make logo for filter cartridge for coffee equipment. Big logo on filter with info below on PeblaQ Water Logo(Big)
Copy attached label verbage from label at Operating Expenses
Size of Label Height 10.25 inches
width 4.75 inches

Target Market(s)

Coffee/Tea Cartridge

Industry/Entity Type

Water Treatment

Font styles to use
Sans Serif

Colors

Designer to choose colors to be used in the design.

Requirements
Must have
• Big Logo for Pebla Q Water
• Easy to write on where install date
Nice to have
• Eye Catching easy to read
Should not have
• no pink

```html
<!DOCTYPE html>
<html lang="en">
<head>
<meta charset="utf-8">
<title>PeblaQ Water – Anti-Scale Cartridge Label</title>
<link href="https://fonts.googleapis.com/css2?family=Open+Sans:wght@400;600;700&display=swap" rel="stylesheet">
<style>
  :root {
    --page: #e0e0e0;
    --white: #ffffff;
    --navy: #03428a;
    --navy-glow: #0a56b5;
    --ink: #111111;
    --dark: #1c1c1c;
    --accent: #2a7be4;
    --brand: #1d5aa8;
  }
  * { margin: 0; padding: 0; box-sizing: border-box; }
  html, body { width: 927px; height: 1200px; overflow: hidden; background: var(--page); }
  body { font-family: "Open Sans", Arial, sans-serif; position: relative; }

  .label {
    position: absolute; left: 205px; top: 40px;
    width: 518px; height: 1120px;
    background: var(--white); overflow: hidden;
  }
  .abs { position: absolute; }

  .brand {
    left: 0; top: 0; width: 518px; height: 160px;
    display: flex; align-items: center; justify-content: center;
  }
  .brand-name {
    font-weight: 700; font-size: 54px; color: var(--brand);
    letter-spacing: 1px; white-space: nowrap;
  }

  .title-band { left: 0; top: 160px; width: 518px; height: 102px; background: var(--navy); color: var(--white); text-align: center; }
  .title-main { position: absolute; left: 0; right: 0; top: 12px; font-size: 41px; font-weight: 600; letter-spacing: 5px; line-height: 44px; }
  .title-sub { position: absolute; left: 0; right: 0; top: 65px; font-size: 32px; font-weight: 600; letter-spacing: 2.2px; line-height: 34px; }

  .tagline { left: 0; top: 272px; width: 518px; text-align: center; font-size: 20.5px; font-weight: 600; line-height: 25px; color: var(--ink); }

  .dates { left: 76px; top: 331px; font-size: 20.5px; font-weight: 700; line-height: 26px; color: var(--ink); }
  .date-row { display: flex; align-items: baseline; }
  .date-key { width: 169px; white-space: pre; }
  .date-line { display: inline-block; width: 186px; border-bottom: 2px solid var(--ink); height: 18px; }

  .specs-panel { left: 0; top: 386px; width: 518px; height: 468px; background: var(--navy); overflow: hidden; }
  .panel-texture {
    position: absolute; inset: 0;
    background:
      radial-gradient(circle at 85% 25%, rgba(10,86,181,0.55), rgba(10,86,181,0) 38%),
      radial-gradient(circle at 80% 75%, rgba(10,86,181,0.45), rgba(10,86,181,0) 40%),
      radial-gradient(circle at 5% 25%, rgba(10,86,181,0.3), rgba(10,86,181,0) 35%);
  }

  .panel-text { position: absolute; color: var(--white); font-size: 18px; font-weight: 600; }
  .conditions { left: 57px; top: 16px; line-height: 21.9px; }
  .conditions .item { padding-left: 14px; white-space: nowrap; }
  .conditions .cont { padding-left: 30px; }
  .instructions { left: 24px; top: 198px; width: 471px; line-height: 21.9px; }
  .instructions .just { text-align: justify; text-align-last: justify; }
  .instructions .indent { padding-left: 26px; }

  .fine-print { left: 0; top: 854px; width: 518px; height: 266px; background: var(--dark); }
  .notes { position: absolute; left: 28px; top: 13px; width: 463px; color: var(--white); font-size: 16.3px; line-height: 20.2px; }
  .notes .head { color: var(--accent); font-weight: 600; }
  .notes .just { text-align: justify; text-align-last: justify; }
  .notes .gap { height: 20px; }
</style>
</head>
<body>
  <div class="label">
    <div class="abs brand"><span class="brand-name">PeblaQ Water</span></div>

    <div class="abs title-band">
      <div class="title-main">ANTI-SCALE</div>
      <div class="title-sub">Water Filtration System</div>
    </div>

    <div class="abs tagline">Hard Scale Prevention, Chlorine Taste &amp;<br>Odor / Sediment Reduction</div>

    <div class="abs dates">
      <div class="date-row"><span class="date-key">Date Installed:</span><span class="date-line"></span></div>
      <div class="date-row"><span class="date-key">Change Date   :</span><span class="date-line"></span></div>
    </div>

    <div class="abs specs-panel">
      <div class="panel-texture" role="img" aria-label="Decorative water bubble pattern"></div>

      <div class="panel-text conditions">
        <div>OPERATING CONDITIONS:</div>
        <div class="item">• Flow Rate: 1 GPM</div>
        <div class="item">• Presuure: 30 - 120 psi</div>
        <div class="item">• Temperature: 40 -100 F</div>
        <div class="item">• Filtration: 5 microns</div>
        <div class="item">• Capacity: 3,170 gallons</div>
        <div class="item">• Function: Chemical / Mechanical</div>
        <div class="cont">Reduction &amp; Hard Scale Prevention</div>
      </div>

      <div class="panel-text instructions">
        <div>INSTALLATION INSTRUCTIONS:</div>
        <div>1. Shut off water supply.</div>
        <div class="just">2. Rotate the old cartridge counter clockwise 1/4</div>
        <div>turn and pull it out.</div>
        <div class="just">3. Insert the new cartridge into the filter head and</div>
        <div>rotae clockwise 1/4 turn.</div>
        <div>4. Place the cartridge to the vertical position.</div>
        <div>5. Turn on the water ad check for leak.</div>
        <div class="indent">If leaks occur, repeat step 1,2,3,4</div>
        <div class="indent">If leaks perist, discontinue use and</div>
        <div class="indent">call your supporting dealer</div>
        <div>6. Flush filter until water runs.</div>
      </div>
    </div>

    <div class="abs fine-print">
      <div class="notes">
        <div class="head">NOTICE:</div>
        <div class="just">1. Do not use with water that is microbiologically unsafe or</div>
        <div class="just">of unknown adequats disinfection before or after the</div>
        <div>sytem.</div>
        <div>2. For cold water only.</div>
        <div class="just">3. Replace cartridge at the rated capacity or if there is a</div>
        <div>noticeable reduction in flow.</div>
        <div class="gap"></div>
        <div class="head">WARRANTY:</div>
        <div class="just">The warranty covers for defects in material and</div>
        <div class="just">workmanship only for a period of 12 months from</div>
        <div>purchasing date.</div>
      </div>
    </div>
  </div>
</body>
</html>
```